Bold Website Redesign for a Disruptive Training Brand

Brightmoor Labs is a bold, no-fluff sales & leadership training company powered by AI-driven practice and behavioral science. We’ve already built our website structure and copy in Craftly.io — now we need a designer to fully transform the visual design across all pages (Home, Approach, Programs, About, Contact).
We’re looking for a modern, memorable, high-performance aesthetic that blends human energy, science, and tech without feeling corporate or safe. Clean, bold typography, fluid layout, strong emotional hero moments, subtle motion, and imagery that mixes real people with abstract scientific/tech visuals.Because our clients are primarily North American, please ensure any human photography or AI-generated imagery reflects a North American business context and demographics (modern, diverse, and realistic).

Your job is visual redesign only — no coding required.
The final design must be practical to rebuild inside Craftly.io.

A full, detailed creative brief (plus logo files) is included in the uploaded files.
If you can bring a mix of edge, intelligence, and strong visual storytelling, we’d love to see your work.

Website is already built in Craftly.io at - https://brightmoor-website-tempdesign.craftly.app — structure is set, visuals need redesign.

```html
<!DOCTYPE html>
<html lang="en">
<head>
<meta charset="utf-8">
<title>Brightmoor Labs — AI-Driven Sales & Leadership Training</title>
<link href="https://fonts.googleapis.com/css2?family=Lexend:wght@400;500;600;700&family=Poppins:wght@400;500;600&display=swap" rel="stylesheet">
<style>
:root{
  --blue:#4568b5;
  --blue-dark:#34549b;
  --blue-soft:#6f8fd6;
  --sky:#4bbde9;
  --ink:#1c1f26;
  --muted:#6b7280;
  --line:#d8dce3;
  --panel:#f2f3f5;
  --footer:#262a33;
  --white:#ffffff;
}
*{box-sizing:border-box;margin:0;padding:0}
html,body{width:1200px;height:4938px;overflow:hidden}
body{font-family:"Poppins",sans-serif;color:var(--ink);background:var(--white);position:relative}
.abs{position:absolute}
h1,h2,h3,.display{font-family:"Lexend",sans-serif;font-weight:500}

/* header */
.brand{left:153px;top:12px;display:flex;align-items:center;gap:10px}
.brand-mark{width:22px;height:22px;background:var(--blue)}
.brand-name{font-family:"Lexend",sans-serif;font-weight:600;font-size:15px;color:var(--ink);letter-spacing:.5px}
.topinfo{top:14px;left:640px;display:flex;gap:26px;font-size:9px;color:var(--ink)}
.topinfo span{display:flex;align-items:center;gap:5px}
.navbar{left:278px;top:42px;width:922px;height:50px;background:var(--sky)}
.nav{left:310px;top:42px;height:50px;display:flex;align-items:center;gap:0}
.nav a{color:var(--white);font-size:12px;font-weight:600;text-decoration:none;width:140px}
.btn-contact{left:932px;top:52px;width:118px;height:38px;background:var(--blue);color:var(--white);font-size:12px;display:flex;align-items:center;justify-content:center;border-radius:3px}

/* hero */
.hero{left:0;top:77px;width:1200px;height:607px;overflow:hidden;background:linear-gradient(100deg,#5477c6 0%,#4a6cbc 45%,#6f8ccf 100%)}
.hero-photo{position:absolute;right:0;top:0;width:720px;height:607px;background:linear-gradient(160deg,#c9d4e3,#7e8fa8 55%,#3a4660);clip-path:polygon(32% 0,100% 0,100% 100%,0 100%)}
.hero-title{left:151px;top:208px;font-family:"Lexend",sans-serif;font-weight:600;font-size:60px;line-height:75px;color:var(--white);text-transform:uppercase;text-shadow:0 3px 6px rgba(0,0,0,.25)}
.hero-sub{left:151px;top:450px;width:390px;font-size:10px;line-height:16px;color:var(--white)}
.btn{display:flex;align-items:center;justify-content:center;font-size:12px;border-radius:3px}
.btn-white{left:151px;top:523px;width:165px;height:33px;background:var(--white);color:var(--ink)}
.btn-ghost{left:330px;top:523px;width:155px;height:33px;border:1px solid rgba(255,255,255,.7);color:var(--white)}

/* science */
.photo{background:linear-gradient(160deg,#cdd6e2,#8c9ab0 60%,#5b6679);border-radius:4px}
.call-card{left:184px;top:1160px;width:178px;height:59px;background:var(--sky);border-radius:4px;display:flex;align-items:center;gap:12px;padding:0 14px;color:var(--white)}
.call-icon{width:32px;height:32px;background:rgba(255,255,255,.25);border-radius:4px;display:flex;align-items:center;justify-content:center}
.call-card small{display:block;font-size:9px;opacity:.85}
.call-card b{font-size:13px;font-weight:600}
.h-section{font-size:52px;line-height:60px;color:var(--ink);font-weight:400}
.para{font-size:11px;line-height:18px;color:var(--muted)}
.quote{left:613px;top:978px;width:418px;height:71px;background:var(--panel);border-left:4px solid var(--blue);padding:14px 24px;font-size:12px;line-height:20px;color:var(--ink);border-radius:3px}
.ticks{left:613px;top:1078px;list-style:none;font-size:12px;color:#444}
.ticks li{display:flex;align-items:center;gap:12px;height:32px}
.btn-blue{background:var(--blue);color:var(--white)}

/* programs */
.center-h{left:0;width:1200px;text-align:center}
.prog{width:260px;text-align:center}
.prog-num{font-family:"Lexend",sans-serif;font-weight:500;font-size:135px;line-height:120px;height:118px;overflow:hidden;background:linear-gradient(180deg,#3fbde8 0%,#8fd9f3 55%,#ffffff 100%);-webkit-background-clip:text;background-clip:text;color:transparent}
.prog-rule{height:6px;margin:0 30px;border-radius:50%;background:radial-gradient(ellipse at center,rgba(0,0,0,.18),transparent 70%)}
.prog h3{font-size:25px;line-height:28px;font-weight:400;margin-top:28px}
.prog p{font-size:11px;line-height:15px;margin-top:16px;color:#333}

/* future */
.future-band{left:0;top:1879px;width:1200px;height:734px;background:linear-gradient(180deg,#4a6cbc,#3d5fae)}
.future-title{left:151px;top:1948px;font-family:"Lexend",sans-serif;font-weight:600;font-size:52px;line-height:60px;color:var(--white);text-shadow:0 3px 6px rgba(0,0,0,.2)}
.future-sub{left:151px;top:2098px;width:460px;font-size:11px;line-height:18px;color:var(--white)}
.feature-card{left:151px;top:2162px;width:459px;height:549px;background:var(--white);border-radius:8px;box-shadow:0 6px 20px rgba(0,0,0,.12);padding:36px 20px 0}
.feature{height:128px}
.feature-head{display:flex;align-items:center;gap:16px}
.feature-num{width:40px;height:40px;background:var(--sky);color:var(--white);font-size:15px;font-weight:600;display:flex;align-items:center;justify-content:center;border-radius:4px}
.feature-head h3{font-size:24px;font-weight:400}
.feature p{font-size:11px;line-height:19px;color:var(--muted);margin-top:12px;width:410px}
.tech-photo{background:linear-gradient(135deg,#0d2a55,#1f6fbf 55%,#7fd0f5);border-radius:8px}
.team-photo{background:linear-gradient(160deg,#c8d3e0,#8a9cb8 60%,#4d5d7a);border-radius:8px}

/* blog */
.post{width:213px;height:307px;background:var(--white);border-radius:6px;overflow:hidden}
.post.raised{box-shadow:0 4px 14px rgba(0,0,0,.12)}
.post-img{height:201px;background:linear-gradient(160deg,#b9c3cf,#7a8597 60%,#4b5262)}
.post-body{padding:10px}
.post-date{font-size:9px;color:var(--muted)}
.post h4{font-family:"Lexend",sans-serif;font-weight:500;font-size:16px;margin-top:10px}
.post p{font-size:9.5px;line-height:15px;color:var(--muted);margin-top:6px}

/* testimonials */
.test-band{left:498px;top:3378px;width:552px;height:379px;background:linear-gradient(135deg,#4b6dbd,#6b8ad0)}
.tcard{width:265px;height:303px;background:var(--white);box-shadow:0 6px 18px rgba(0,0,0,.1);padding:22px 22px}
.qmark{width:30px;height:30px;background:#eef0f6;color:var(--blue);font-weight:700;font-size:14px;display:flex;align-items:center;justify-content:center}
.stars{position:absolute;right:22px;top:30px;color:#f5b82e;font-size:14px;letter-spacing:1px}
.tcard h4{font-family:"Lexend",sans-serif;font-weight:500;font-size:16px;line-height:19px;margin-top:20px}
.tcard p{font-size:9px;line-height:17px;color:var(--muted);margin-top:14px}
.person{display:flex;align-items:center;gap:12px;margin-top:26px}
.avatar{width:40px;height:40px;border-radius:50%;background:#c9d1de}
.person b{display:block;font-size:9px;font-weight:600}
.person small{font-size:8px;color:var(--sky)}
.test-title{left:730px;top:3440px;font-family:"Lexend",sans-serif;font-weight:600;font-size:52px;line-height:58px;color:var(--white);text-shadow:0 3px 6px rgba(0,0,0,.2)}
.btn-read{left:730px;top:3661px;width:163px;height:33px;background:var(--white);color:var(--ink);font-size:11px}

/* contact */
.contact-photo{left:151px;top:3974px;width:311px;height:523px;background:linear-gradient(160deg,#c5cfdc,#8795ab 55%,#4b5872)}
.form-panel{left:462px;top:3974px;width:588px;height:523px;background:var(--white);box-shadow:0 6px 20px rgba(0,0,0,.08)}
.form-title{left:506px;top:4002px;font-size:36px;font-weight:400}
.field-label{left:510px;font-size:11px;color:#333}
.field{left:506px;width:502px;height:40px;border:1px solid #9aa1ab;border-radius:4px;background:#f7f7f8}
.btn-submit{left:506px;top:4432px;width:502px;height:37px;background:var(--blue);color:var(--white);font-size:12px;font-weight:600;border-radius:4px}

/* footer */
.footer{left:0;top:4593px;width:1200px;height:345px;background:linear-gradient(90deg,#232730 0%,#2c313b 55%,#3a404b 100%)}
.footer-brand{left:151px;top:4680px;display:flex;align-items:center;gap:12px}
.footer-brand .brand-mark{width:30px;height:30px;background:var(--white)}
.footer-brand span{font-family:"Lexend",sans-serif;font-weight:600;font-size:26px;color:var(--white);letter-spacing:1px}
.footer-text{left:151px;top:4786px;width:360px;font-size:11px;line-height:19px;color:var(--white)}
.footer-right{left:773px;top:4694px;width:280px;font-size:11px;line-height:22px;color:var(--white)}
.social{left:773px;top:4783px;display:flex;gap:14px}
.social span{width:30px;height:30px;border:1.5px solid var(--white);border-radius:50%}
.footer-nav{left:155px;top:4850px;display:flex;font-size:11px;color:var(--white)}
.footer-nav span{width:137px}
.footer-rule{left:151px;top:4892px;width:899px;height:1px;background:rgba(255,255,255,.4)}
.footer-legal{left:323px;top:4908px;display:flex;gap:32px;font-size:10px;color:#cfd3da}
</style>
</head>
<body>

<!-- Header -->
<div class="abs brand"><span class="brand-mark"></span><span class="brand-name">BRIGHTMOOR LABS</span></div>
<div class="abs topinfo">
  <span><svg width="9" height="11" viewBox="0 0 9 11"><path d="M4.5 0.5a3.5 3.5 0 0 1 3.5 3.5c0 2.6-3.5 6.5-3.5 6.5S1 6.6 1 4A3.5 3.5 0 0 1 4.5.5z" fill="none" stroke="#4568b5"/></svg>Lorem Ipsum Dolor Sit Amet Consectetur</span>
  <span><svg width="11" height="8" viewBox="0 0 11 8"><rect x=".5" y=".5" width="10" height="7" fill="none" stroke="#4568b5"/><path d="M.5.5l5 4 5-4" fill="none" stroke="#4568b5"/></svg>hello@brightmoorlabs.com</span>
  <span><svg width="10" height="10" viewBox="0 0 10 10"><path d="M2 1l2 2-1 1.5a6 6 0 0 0 2.5 2.5L7 6l2 2-1.5 1.5C4 9 1 6 .5 2.5z" fill="none" stroke="#4568b5"/></svg>+1 (415) 555-0148</span>
</div>
<div class="abs navbar"></div>
<nav class="abs nav"><a>Home</a><a>Approach</a><a>Programs</a><a>About Us</a></nav>
<div class="abs btn-contact">Contact Us</div>

<!-- Hero -->
<section class="abs hero">
  <div class="hero-photo" role="img" aria-label="Smiling businesswoman and colleague reviewing a tablet in a bright office"></div>
  <svg class="abs" style="left:0;top:0" width="1200" height="607"><line x1="790" y1="0" x2="556" y2="520" stroke="#fff" stroke-width="7"/></svg>
</section>
<h1 class="abs hero-title">AI-Driven Sales<br>&amp; Leadership<br>Training</h1>
<p class="abs hero-sub">Powered By AI-Driven Practice And Behavioral Science. Bold. Confident. No Fluff. Powered By AI-Driven Practice And Behavioral Science. Bold. Confident. No Fluff.</p>
<div class="abs btn btn-white">Start Your Training</div>
<div class="abs btn btn-ghost">See Our Programs</div>

<!-- Science Meets Human Potential -->
<div class="abs photo" style="left:153px;top:782px;width:242px;height:418px" role="img" aria-label="Woman presenting at a laptop in a meeting room"></div>
<div class="abs photo" style="left:406px;top:782px;width:188px;height:441px" role="img" aria-label="Colleagues collaborating over a laptop in an office"></div>
<div class="abs call-card">
  <div class="call-icon"><svg width="16" height="14" viewBox="0 0 16 14"><rect x="1" y="1" width="10" height="7" rx="1" fill="none" stroke="#fff" stroke-width="1.4"/><rect x="5" y="5" width="10" height="7" rx="1" fill="#fff"/></svg></div>
  <div><small>Call for Questions</small><b>+1 415 555 0192</b></div>
</div>
<h2 class="abs h-section" style="left:613px;top:780px">Science Meets<br>Human Potential</h2>
<p class="abs para" style="left:613px;top:917px;width:420px">There are many variations of passages about of lorem ipsum avalable, but the majority have suffered alteration free in some form</p>
<div class="abs quote">The Generated Lorem Ipsum Is Therfore Always Free From Repetition, Injected Humour, Or</div>
<ul class="abs ticks">
  <li><svg width="14" height="14" viewBox="0 0 14 14"><circle cx="7" cy="7" r="7" fill="#4bbde9"/><path d="M4 7.2l2 2 4-4" stroke="#fff" stroke-width="1.6" fill="none"/></svg>AI-Driven Simulations For Realistic Practice</li>
  <li><svg width="14" height="14" viewBox="0 0 14 14"><circle cx="7" cy="7" r="7" fill="#4bbde9"/><path d="M4 7.2l2 2 4-4" stroke="#fff" stroke-width="1.6" fill="none"/></svg>Behavioral Science Techniques For Lasting Results</li>
  <li><svg width="14" height="14" viewBox="0 0 14 14"><circle cx="7" cy="7" r="7" fill="#4bbde9"/><path d="M4 7.2l2 2 4-4" stroke="#fff" stroke-width="1.6" fill="none"/></svg>Real-Time Feedback To Improve Skills Quickly</li>
</ul>
<div class="abs btn btn-blue" style="left:613px;top:1196px;width:119px;height:31px;font-size:11px">Learn More</div>

<!-- Programs -->
<h2 class="abs center-h h-section" style="top:1318px;font-size:50px">Train Smarter, Lead Better</h2>
<div class="abs prog" style="left:133px;top:1476px">
  <div class="prog-num">01</div><div class="prog-rule"></div>
  <h3>Sales<br>Acceleration</h3><p>AI-Guided Exercises To Improve<br>Closing Rates</p>
</div>
<div class="abs prog" style="left:468px;top:1476px">
  <div class="prog-num">02</div><div class="prog-rule"></div>
  <h3>Leadership<br>Excellence</h3><p>Behavioral Science-Based<br>Leadership Coaching</p>
</div>
<div class="abs prog" style="left:807px;top:1476px">
  <div class="prog-num">03</div><div class="prog-rule"></div>
  <h3>Team<br>Performance</h3><p>Real-Time Team Simulations And<br>Feedback</p>
</div>
<div class="abs btn btn-blue" style="left:521px;top:1754px;width:158px;height:31px;font-size:11px">See All Programs</div>

<!-- The Future of Training -->
<div class="abs future-band"></div>
<h2 class="abs future-title">The Future Of<br>Training, Today</h2>
<p class="abs future-sub">Sed ut perspiciatis unde omnis iste natus error sit voluptat accusantium doloremque laudantium, totam rem operiam,</p>
<div class="abs feature-card">
  <div class="feature"><div class="feature-head"><span class="feature-num">1</span><h3>AI-Powered</h3></div><p>Complete roof installation for a home or building — with quality materials and expert craftsmanship.</p></div>
  <div class="feature"><div class="feature-head"><span class="feature-num">2</span><h3>Science-Backed</h3></div><p>Full replacement of old, damaged, or sagging roofs with modern materials for improved durability and insulation.</p></div>
  <div class="feature"><div class="feature-head"><span class="feature-num">3</span><h3>Real Practice</h3></div><p>Leaks, Missing Tiles, and Storm Damage Repair — Quick Response and Affordable Service.</p></div>
  <div class="feature"><div class="feature-head"><span class="feature-num">4</span><h3>High Impact</h3></div><p>Leaks, Missing Tiles, and Storm Damage Repair — Quick Response and Affordable Service.</p></div>
</div>
<div class="abs tech-photo" style="left:646px;top:1955px;width:404px;height:361px" role="img" aria-label="Professional interacting with a holographic AI data interface"></div>
<div class="abs team-photo" style="left:646px;top:2348px;width:404px;height:363px" role="img" aria-label="Diverse team smiling together around a meeting table"></div>

<!-- Blog -->
<h2 class="abs center-h h-section" style="top:2803px">Smart Thinking For Sales And<br>Leadership</h2>
<article class="abs post" style="left:151px;top:2975px"><div class="post-img" role="img" aria-label="Team reviewing documents together"></div><div class="post-body"><div class="post-date">January 23,2024</div><h4>Leadership Posts</h4><p>Lorem Ipsum Dolor Sit Amet Consectetur. Nam Ac Ornare Sit</p></div></article>
<article class="abs post" style="left:380px;top:2975px"><div class="post-img" role="img" aria-label="Colleagues working on laptops at a shared desk"></div><div class="post-body"><div class="post-date">February 11,2024</div><h4>Leadership Posts</h4><p>Lorem Ipsum Dolor Sit Amet Consectetur. Nam Ac</p></div></article>
<article class="abs post raised" style="left:608px;top:2975px"><div class="post-img" role="img" aria-label="Group discussion around a laptop in a dim office"></div><div class="post-body"><div class="post-date" style="color:#222">February 29,2023</div><h4>Leadership Posts</h4><p>Lorem Ipsum Dolor Sit. Consectetur. Nam Ac Ornare Sit Enim Sem</p></div></article>
<article class="abs post" style="left:836px;top:2975px"><div class="post-img" role="img" aria-label="Boardroom meeting with presentation screen"></div><div class="post-body"><div class="post-date">March 26,2024</div><h4>Leadership Posts</h4><p>Lorem Ipsum Dolor Sit Amet Consectetur. Nam</p></div></article>

<!-- Testimonials -->
<div class="abs test-band"></div>
<div class="abs tcard" style="left:151px;top:3416px">
  <div class="qmark">“</div><span class="stars">★★★★★</span>
  <h4>Sejuk is the most<br>professional</h4>
  <p>Duis aute irure dolor in reprehen voluptate velit esse cillum dolore eu fugiat nulla pariatur non proident sunt culpa qui officia deserunt. Sed ut perspiciatis unde omnis iste natus error</p>
  <div class="person"><span class="avatar" role="img" aria-label="Client portrait"></span><div><b>DANA WHITFIELD</b><small>Founder Lumo</small></div></div>
</div>
<div class="abs tcard" style="left:437px;top:3416px">
  <div class="qmark">“</div><span class="stars">★★★★★</span>
  <h4>Sejuk is the most<br>professional</h4>
  <p>Duis aute irure dolor in reprehen voluptate velit esse cillum dolore eu fugiat nulla pariatur non proident sunt culpa qui officia deserunt. Sed ut perspiciatis unde omnis iste natus error</p>
  <div class="person"><span class="avatar" role="img" aria-label="Client portrait"></span><div><b>DANA WHITFIELD</b><small>Founder Lumo</small></div></div>
</div>
<h2 class="abs test-title">Real<br>Results.<br>Real People</h2>
<div class="abs btn btn-read">Read More Stories</div>

<!-- Contact -->
<h2 class="abs center-h h-section" style="top:3850px">Ready To Transform Your Team</h2>
<div class="abs contact-photo" role="img" aria-label="Smiling professionals shaking hands in an office"></div>
<div class="abs form-panel"></div>
<h3 class="abs form-title">Contact Form</h3>
<label class="abs field-label" style="top:4078px">Name</label><div class="abs field" style="top:4099px"></div>
<label class="abs field-label" style="top:4165px">Email</label><div class="abs field" style="top:4186px"></div>
<label class="abs field-label" style="top:4250px">Addess</label><div class="abs field" style="top:4271px"></div>
<label class="abs field-label" style="top:4336px">Phone Number</label><div class="abs field" style="top:4355px"></div>
<div class="abs btn btn-submit">Submit</div>

<!-- Footer -->
<footer class="abs footer"></footer>
<div class="abs footer-brand"><span class="brand-mark"></span><span>BRIGHTMOOR LABS</span></div>
<p class="abs footer-text">Lorem Ipsum Dolor Sit Amet Consectetur. Leo Ornare Purus Id Ut Sem.</p>
<p class="abs footer-right">Lorem Ipsum Dolor Sit Amet Consectetur. Aliquam Dolor Consequat Eu Ac Mus Orci Amet Erat Molestie Vitae.</p>
<div class="abs social"><span></span><span></span><span></span><span></span></div>
<div class="abs footer-nav"><span>Home</span><span>Approach</span><span>Programs</span><span>About Us</span><span>Contact Us</span></div>
<div class="abs footer-rule"></div>
<div class="abs footer-legal"><span>Copyright © 2025 All Right Reserved</span><span>Privacy Policy</span><span>Terms Of Service</span><span>Cookies Settings</span></div>

</body>
</html>
```